Need Bold, Hip Card for Concert Ticket Website Velvet Stubs!

Hi there! I am putting together a business/website that sells event tickets (mostly concerts, but also some sports and theater). Think PassDepot, but much smaller. The site is called Velvet Stubs. I have a new logo (attached, with black/red/white color scheme), and am looking for a modern/cool/original business card design. Note that I am thinking of having the card itself in the shape of a ticket (die cut), so you may want to keep that in mind when designing, but I'm not set on that. I'm also open to alternative card sizes, thicknesses, glossy, spot UV, etc. in order to stand out. I'm attaching a potential die cut template and a sample card using that template in case you want to work with that.
Target Market(s)
Music fans, people that like going to see live events
Industry/Entity Type
Entertainment
Contact Information for Business Card
Information that I'd like to have:
website address - www.velvetstubs-example.com
phone number: 1-833-5VELVETS (835-3887)
my name - Delia Hart
Look and feel
Each slider illustrates characteristics of the customer's brand and the style your logo design should communicate.

```html
<!DOCTYPE html>
<html lang="en">
<head>
<meta charset="utf-8">
<title>Velvet Stubs – Business Card</title>
<link rel="stylesheet" href="https://fonts.googleapis.com/css2?family=Montserrat:wght@800&family=Arimo:wght@400&display=swap">
<style>
  :root {
    --backdrop: #1c1c1c;
    --card: #050505;
    --velvet-red: #8e0a0a;
    --white: #ffffff;
    --silver: #bcbcbc;
  }
  * { margin: 0; padding: 0; box-sizing: border-box; }
  html, body { width: 1200px; height: 1200px; overflow: hidden; }
  body {
    background: var(--backdrop);
    display: flex;
    flex-direction: column;
    align-items: center;
    justify-content: center;
    gap: 60px;
  }
  .card {
    position: relative;
    width: 880px;
    height: 503px;
    background: var(--card);
    box-shadow: 0 12px 30px rgba(0,0,0,0.6);
  }
  .card__frame {
    position: absolute;
    inset: 28px;
    border: 3px solid var(--velvet-red);
  }
  .brand {
    display: flex;
    align-items: center;
    gap: 18px;
  }
  .brand__square {
    flex: none;
    width: 64px;
    height: 64px;
  }
  .brand-name {
    font-family: "Montserrat", sans-serif;
    font-weight: 800;
    text-transform: uppercase;
    letter-spacing: 2px;
    line-height: 1;
    white-space: nowrap;
  }
  .card--back .brand {
    position: absolute;
    left: 50%;
    top: 50%;
    transform: translate(-50%, -60%);
  }
  .card--back .brand__square { background: var(--silver); width: 72px; height: 72px; }
  .card--back .brand-name { font-size: 60px; color: var(--silver); }

  .card--front .brand {
    position: absolute;
    left: 70px;
    top: 72px;
  }
  .card--front .brand__square { background: var(--velvet-red); width: 54px; height: 54px; }
  .card--front .brand-name { font-size: 44px; color: var(--velvet-red); }

  .brand-mark-area {
    position: absolute;
    right: 80px;
    bottom: 64px;
    width: 290px;
    height: 290px;
    background: var(--velvet-red);
  }
  .contact {
    position: absolute;
    left: 70px;
    bottom: 96px;
    width: 460px;
  }
  .contact__name {
    font-family: "Montserrat", sans-serif;
    font-weight: 800;
    font-size: 32px;
    color: var(--white);
    text-transform: uppercase;
    letter-spacing: 1px;
  }
  .contact__web {
    font-family: "Arimo", sans-serif;
    font-size: 24px;
    color: var(--velvet-red);
    text-transform: uppercase;
    margin-top: 8px;
  }
  .contact__phone {
    font-family: "Arimo", sans-serif;
    font-size: 20px;
    color: var(--white);
    margin-top: 8px;
  }
</style>
</head>
<body>
  <section class="card card--back">
    <div class="card__frame"></div>
    <div class="brand">
      <span class="brand__square"></span>
      <span class="brand-name">Velvet Stubs</span>
    </div>
  </section>

  <section class="card card--front">
    <div class="card__frame"></div>
    <div class="brand">
      <span class="brand__square"></span>
      <span class="brand-name">Velvet Stubs</span>
    </div>
    <div class="brand-mark-area" role="img" aria-label="Large Velvet Stubs brand mark"></div>
    <div class="contact">
      <div class="contact__name">Delia Hart</div>
      <div class="contact__web">www.velvetstubs-example.com</div>
      <div class="contact__phone">Phone: 1-833-5VELVETS (835-3887)</div>
    </div>
  </section>
</body>
</html>
```